New Real Estate business seek modern cutting edge stationery Design for Letterhead,Presentation fold

We need full stationary designs for new real estate company from Toronto Ontario. We would like a very cool, new, sleek, modern cutting edge design design for email signature, letterhead, envelope and presentation folder.

Let your imagination run wild, looking for a really cool package

Attached is all versions of my logo, the main colours are Red,white and black.

Industry/Entity Type

Real Estate

Requirements
Must have
• Envelope must have a Top secret stamp water marked into the middle
• Presentation folder must have SOLD sign inside
• Follow logo colour seem .
• make all txt editable

```html
<!DOCTYPE html>
<html lang="en">
<head>
<meta charset="utf-8">
<title>Presentation Folder – Inside Spread</title>
<link rel="stylesheet" href="https://fonts.googleapis.com/css2?family=Josefin+Sans:wght@300;400&display=swap">
<style>
  :root {
    --brand-red: #ed1c24;
    --paper: #ffffff;
    --fold-line: #5a5a5a;
    --ink-light: #ffffff;
  }
  html, body {
    margin: 0;
    padding: 0;
    width: 1200px;
    height: 821px;
    overflow: hidden;
    background: var(--paper);
  }
  .folder-spread {
    position: relative;
    width: 1200px;
    height: 821px;
    background: var(--paper);
    font-family: "Josefin Sans", sans-serif;
  }
  .pocket-shapes {
    position: absolute;
    inset: 0;
  }
  .pocket-shapes .pocket { fill: var(--brand-red); }
  .pocket-shapes .fold { stroke: var(--fold-line); stroke-width: 1.5; }
  .sold-label {
    position: absolute;
    left: 174px;
    top: 699px;
    margin: 0;
    font-weight: 300;
    font-size: 48px;
    line-height: 1;
    letter-spacing: 0.5em;
    color: var(--ink-light);
  }
  .brand-name {
    position: absolute;
    right: 34px;
    top: 706px;
    margin: 0;
    font-weight: 400;
    font-size: 30px;
    line-height: 1;
    letter-spacing: 0.04em;
    color: var(--ink-light);
  }
</style>
</head>
<body>
  <main class="folder-spread">
    <svg class="pocket-shapes" width="1200" height="821" viewBox="0 0 1200 821" aria-hidden="true">
      <line class="fold" x1="600" y1="0" x2="600" y2="821"/>
      <polygon class="pocket pocket-left" points="0,621 487,621 598,821 0,821"/>
      <polygon class="pocket pocket-right" points="712,621 1200,621 1200,821 602,821"/>
    </svg>
    <p class="sold-label">SOLD</p>
    <p class="brand-name">Harbourline</p>
  </main>
</body>
</html>
```